Mexican construction company needs a business card design

We need a business card design for a company based in Monterrey, Mexico called:

Desarrollos Tolvani S.A. de C.V.

The company is in the construction business and I would like the businees card to be simple and concise. Please use white background and blue or black text color that say:

"Proyectos de Construcción"-- (Brief description of business)
" Rodrigo Ulloa Benítez"--- (My name)
"rulloab@correovelo.mx"-- (My email)
"C: (81) 82 19 57 46"-- (My cell)
"O: (81) 86 72 13 95"-- (Office phone)

Please use only the colors of my company that are attached

Please make the back of the business card blue (same blue from logo) and use the logo.

Thanks!

```html
<!DOCTYPE html>
<html lang="es">
<head>
<meta charset="utf-8">
<title>Desarrollos Tolvani — Tarjeta de presentación</title>
<link rel="stylesheet" href="https://fonts.googleapis.com/css2?family=Exo+2:wght@400;600;700&display=swap">
<style>
  :root {
    --page-bg: #e6e4e1;
    --card-bg: #ffffff;
    --navy: #1c1b3a;
    --navy-deep: #121129;
    --silver: #b9bcc4;
    --silver-dark: #6e7280;
    --ink: #1f1e3d;
    --name-color: #e4e2e6;
    --detail-color: #a79f9c;
    --label-color: #c08f8a;
  }
  * { box-sizing: border-box; margin: 0; padding: 0; }
  html, body {
    width: 1200px;
    height: 969px;
    overflow: hidden;
    background: var(--page-bg);
    font-family: "Exo 2", Arial, sans-serif;
  }
  .business-card {
    position: absolute;
    left: 100px;
    top: 200px;
    width: 1000px;
    height: 568px;
    background: var(--card-bg);
    box-shadow: 0 18px 40px rgba(0, 0, 0, 0.18);
    overflow: hidden;
  }
  .card-band {
    position: absolute;
    inset: 0;
    width: 1000px;
    height: 568px;
  }
  .brand {
    position: absolute;
    left: 300px;
    top: 96px;
    display: flex;
    align-items: center;
    gap: 34px;
  }
  .brand-square {
    width: 96px;
    height: 96px;
    background: var(--ink);
  }
  .brand-name {
    color: var(--ink);
    font-weight: 700;
    font-size: 52px;
    line-height: 1;
    letter-spacing: 2px;
    text-transform: uppercase;
  }
  .contact {
    position: absolute;
    left: 0;
    right: 0;
    top: 350px;
    text-align: center;
  }
  .contact-name {
    color: var(--name-color);
    font-size: 31px;
    font-weight: 600;
    letter-spacing: 0.5px;
  }
  .contact-role {
    color: var(--detail-color);
    font-size: 22px;
    margin-top: 4px;
  }
  .contact-phones, .contact-email {
    color: var(--detail-color);
    font-size: 22px;
    letter-spacing: 1px;
  }
  .contact-phones { margin-top: 36px; }
  .contact-email { margin-top: 12px; }
  .label { color: var(--label-color); font-weight: 600; }
  .contact-phones .label + .value { margin-right: 18px; }
</style>
</head>
<body>
  <div class="business-card">
    <svg class="card-band" viewBox="0 0 1000 568" aria-hidden="true">
      <defs>
        <linearGradient id="bandFill" x1="0" y1="0" x2="0" y2="1">
          <stop offset="0" stop-color="#25244a"/>
          <stop offset="1" stop-color="#121129"/>
        </linearGradient>
        <linearGradient id="bevel" x1="0" y1="0" x2="1" y2="0">
          <stop offset="0" stop-color="#6e7280"/>
          <stop offset="0.3" stop-color="#d6d8de"/>
          <stop offset="0.7" stop-color="#9a9ea8"/>
          <stop offset="1" stop-color="#d6d8de"/>
        </linearGradient>
      </defs>
      <polygon points="0,410 205,300 795,300 1000,410 1000,426 0,426" fill="url(#bevel)"/>
      <polygon points="0,424 212,312 788,312 1000,424 1000,568 0,568" fill="url(#bandFill)"/>
    </svg>

    <div class="brand">
      <div class="brand-square"></div>
      <div class="brand-name">Desarrollos<br>Tolvani</div>
    </div>

    <div class="contact">
      <p class="contact-name">Rodrigo Ulloa Benítez</p>
      <p class="contact-role">CEO/Founder</p>
      <p class="contact-phones"><span class="label">P :</span> <span class="value">(81) 86 72 13 95</span> <span class="label">M :</span> <span>(81) 82 19 57 46</span></p>
      <p class="contact-email"><span class="label">W :</span> rulloab@correovelo.mx</p>
    </div>
  </div>
</body>
</html>
```